Letterhead for new real estate company in South Africa named Tallowick

A letterhead with the directors and company details to be editable as these changes often

Target Market(s)

In line with our logo brief and our newly designed logo and corporate fee

Industry/Entity Type

Real Estate

Requirements
Must have
• Details as per the sample letterhead provided.

```html
<!DOCTYPE html>
<html lang="en">
<head>
<meta charset="utf-8">
<title>Tallowick Letterhead</title>
<link href="https://fonts.googleapis.com/css2?family=Open+Sans:wght@400;600;700&family=Montserrat:wght@400;500&family=Tangerine:wght@700&display=swap" rel="stylesheet">
<style>
  :root {
    --backdrop: #d9d9d9;
    --paper: #ffffff;
    --green: #2aa468;
    --green-dark: #26945d;
    --taupe: #6b625a;
    --ink: #3f3f3f;
    --ink-soft: #555555;
  }
  * { box-sizing: border-box; margin: 0; padding: 0; }
  html, body {
    width: 1200px; height: 1159px; overflow: hidden;
    background: var(--backdrop);
  }
  .letterhead {
    position: absolute; left: 204px; top: 20px;
    width: 792px; height: 1119px;
    background: var(--paper);
    font-family: "Open Sans", sans-serif;
    color: var(--ink);
    box-shadow: 0 6px 24px rgba(0,0,0,.18);
  }
  .brand {
    position: absolute; top: 70px; left: 0; right: 0;
    display: flex; justify-content: center; align-items: center; gap: 12px;
  }
  .brand-dot { width: 22px; height: 22px; border-radius: 50%; background: var(--green); }
  .brand-name {
    font-family: "Open Sans", sans-serif; font-weight: 600;
    font-size: 40px; color: var(--green); letter-spacing: 1px; text-transform: uppercase;
  }
  .letter { position: absolute; top: 250px; left: 84px; right: 84px; font-size: 14.5px; line-height: 1.45; }
  .date { margin-bottom: 14px; }
  .recipient { margin-left: 18px; margin-bottom: 12px; }
  .address { margin-left: 30px; margin-bottom: 14px; }
  .salutation { font-weight: 700; font-size: 18px; margin-left: 42px; margin-bottom: 14px; }
  .body { margin-left: 42px; text-align: justify; }
  .body p { margin-bottom: 16px; }
  .closing { position: absolute; top: 810px; left: 146px; font-size: 15px; color: var(--ink-soft); }
  .signature {
    position: absolute; top: 838px; left: 166px;
    font-family: "Tangerine", cursive; font-weight: 700; font-size: 50px; color: var(--ink);
  }
  .directors {
    position: absolute; top: 820px; right: 56px; text-align: right;
    font-family: "Montserrat", sans-serif; font-size: 13px; line-height: 1.75; color: var(--ink);
  }
  .directors .label { color: var(--green); }
  .rule { position: absolute; top: 935px; left: 56px; right: 56px; height: 1.5px; background: var(--green); }
  .company {
    position: absolute; top: 950px; left: 84px;
    font-family: "Montserrat", sans-serif; font-size: 12.5px; line-height: 1.6; color: var(--ink);
  }
  .company .label { color: var(--green); font-weight: 500; }
  .franchise {
    position: absolute; top: 1040px; right: 56px;
    font-family: "Montserrat", sans-serif; font-size: 12.5px; color: var(--ink);
  }
  .footer-band { position: absolute; bottom: 0; left: 0; right: 0; height: 16px; display: flex; }
  .footer-band .green { flex: 1; background: var(--green-dark); }
  .footer-band .taupe { width: 120px; background: var(--taupe); margin-left: 6px; }
</style>
</head>
<body>
  <main class="letterhead">
    <header class="brand">
      <span class="brand-dot"></span>
      <span class="brand-name">Tallowick</span>
    </header>

    <section class="letter">
      <p class="date">June -22-2020</p>
      <p class="recipient">Mr, Peter Lang<br>President</p>
      <p class="address">Mariner Holdings<br>123 Street Name, Suite# 10<br>City, State, 120023</p>
      <p class="salutation">Dear Mr, Peter</p>
      <div class="body">
        <p>Lorem ipsum dolor sit amet, consectetur adipisicing elit, sed do eiusmod tempor incididunt ut labore et dolore magna aliqua. Ut enim ad minim veniam, quis nostrud exercitation ullamco laboris nisi ut aliquip ex ea commodo consequat. Duis aute irure dolor in reprehenderit in voluptate velit esse cillum dolore eu fugiat nulla pariatur.</p>
        <p>Lorem ipsum dolor sit amet, consectetur adipisicing elit, sed do eiusmod tempor incididunt ut labore et dolore magna aliqua. Ut enim ad minim veniam, quis nostrud exercitation ullamco laboris nisi ut aliquip ex ea commodo consequat. Duis aute irure dolor in reprehenderit in voluptate velit esse cillum dolore eu fugiat nulla pariatur.</p>
        <p>Lorem ipsum dolor sit amet, consectetur adipisicing elit, sed do eiusmod tempor incididunt ut labore et dolore magna aliqua. Ut enim ad minim veniam, quis nostrud exercitation ullamco laboris nisi ut aliquip ex ea commodo consequat.</p>
        <p>Excepteur sint occaecat cupidatat non proident, sunt in culpa qui officia deserunt mollit anim id est laborum. re et dolore magnam aliquam quaerat voluptatem.</p>
      </div>
    </section>

    <p class="closing">Regards</p>
    <p class="signature">Daniel Pretorius</p>

    <aside class="directors">
      <span class="label">Director:</span><br>
      R Vermaak<br>
      LN Dlamini-Hart
    </aside>

    <div class="rule"></div>

    <footer class="company">
      Highveld Homes (Pty) Ltd t/a Tallowick Sandton North, Reg No: 2019/458203/07<br>
      Shop B12, Oakridge Centre, Corner Kestrel Road &amp; Willow Lane<br>
      Morningside, South Africa<br>
      <span class="label">Tel:</span> 010 555 0142<br>
      <span class="label">web:</span> www.tallowick.co.za
    </footer>
    <p class="franchise">Each Franchise is independently Owned and operated</p>

    <div class="footer-band"><span class="green"></span><span class="taupe"></span></div>
  </main>
</body>
</html>
```